Belarde's Plumbing, Heating, and AC Buisness card

I need a business card design for my Plumbing Heating and AC company. We are based out of North Windham, CT, and offer residential and light commercial services. I am looking for something that incorporates a water droplet, snowflake, and flame. I would like it to be Modern and different from a typical business card but needs to communicate confidence and security.

```html
<!DOCTYPE html>
<html lang="en">
<head>
<meta charset="utf-8">
<title>Belarde's Plumbing, Heating, and AC — Business Card</title>
<link rel="stylesheet" href="https://fonts.googleapis.com/css2?family=Arimo:wght@400;700&display=swap">
<style>
  :root {
    --page-bg: #d9d9db;
    --card-white: #ffffff;
    --brand-blue: #0a5599;
    --tag-grey: #b4b4b4;
    --stripe-red: #e8322a;
    --stripe-orange: #f08a1c;
    --stripe-yellow: #f5dc0a;
    --footer-text: #ffffff;
  }
  html, body {
    margin: 0;
    padding: 0;
    width: 1200px;
    height: 1000px;
    overflow: hidden;
    background: var(--page-bg);
    font-family: "Arimo", Arial, sans-serif;
  }
  .card {
    position: absolute;
    left: 74px;
    top: 201px;
    width: 1052px;
    height: 598px;
    background: var(--card-white);
    overflow: hidden;
  }
  .brand {
    position: absolute;
    left: 0;
    top: 0;
    width: 100%;
    height: 410px;
    text-align: center;
  }
  .brand-mark {
    position: absolute;
    left: 50%;
    top: 72px;
    width: 104px;
    height: 104px;
    margin-left: -52px;
    border-radius: 50%;
    background: var(--brand-blue);
  }
  .brand-name {
    position: absolute;
    left: 0;
    right: 0;
    top: 262px;
    margin: 0;
    font-size: 92px;
    line-height: 92px;
    font-weight: 700;
    color: var(--brand-blue);
    letter-spacing: 1px;
  }
  .brand-services {
    position: absolute;
    left: 0;
    right: 0;
    top: 362px;
    margin: 0;
    font-size: 28px;
    line-height: 30px;
    font-weight: 700;
    color: var(--tag-grey);
    letter-spacing: 0.5px;
  }
  .brand-services .divider {
    font-weight: 400;
    margin: 0 6px;
  }
  .accent-stripe {
    position: absolute;
    left: 0;
    top: 410px;
    width: 100%;
    height: 19px;
    background: linear-gradient(90deg, var(--stripe-red) 0%, var(--stripe-orange) 35%, var(--stripe-yellow) 100%);
  }
  .contact {
    position: absolute;
    left: 0;
    top: 429px;
    width: 100%;
    height: 169px;
    background: var(--brand-blue);
    color: var(--footer-text);
    text-align: center;
  }
  .contact-line {
    margin: 0;
    white-space: nowrap;
  }
  .contact-primary {
    padding-top: 20px;
    font-size: 34px;
    line-height: 44px;
  }
  .contact-name {
    font-weight: 700;
    font-size: 39px;
    margin-right: 34px;
  }
  .contact-label {
    font-size: 27px;
  }
  .contact-secondary {
    font-size: 31px;
    line-height: 42px;
  }
  .contact-secondary .gap {
    display: inline-block;
    width: 28px;
  }
</style>
</head>
<body>
  <main class="card">
    <section class="brand">
      <div class="brand-mark"></div>
      <h1 class="brand-name">Belarde's</h1>
      <p class="brand-services">PLUMBING<span class="divider">|</span>HEATING<span class="divider">|</span>AC</p>
    </section>
    <div class="accent-stripe"></div>
    <section class="contact">
      <p class="contact-line contact-primary">
        <span class="contact-name">Marco Belarde</span><span class="contact-label">Tel:</span> (067) 555 0148
      </p>
      <p class="contact-line contact-secondary">marco@bphac.com<span class="gap"></span>www.bphac.com</p>
      <p class="contact-line contact-secondary">45 Birch Lane, North Windham, CT</p>
    </section>
  </main>
</body>
</html>
```